Vantorel Silver Gifts needs a Flyer

We need a flyer design for an upcoming trade show we will be participating in.

We sell sterling silver gifts in all categories- baby, mens, bar ware, home, cutlery and more. We would like to get a flyer designed that we can hand out at the show.

The following are few requirements we would like in the flyer:

The flyer must not be too large. An easy handout flyer size
The concept we would like is attached here. It is only a layout of the flyer.
Our brand colors must be part of the flyer- white, red, silver and black
The flyer must be simple and elegant. Show our products clearly and must impress in 1 look
Our logo is attached here as well
Images for the products we would like to insert in the flyer are here
The 4 flap concept is to have 1 flap for each category
Either 1 or 2 images could be used
The layout of the images must be neat
An elegant design is what we would like
Our website: www.vantorel.example - currently we only sell baby gifta and a few ens gifts. However, we would like our flyer to include all categories.
Contact details and website should also be included:
Website: www.vantorel.example
Email : info@vantorel.example
Buyer Contact: 555-318-2947

Categories:
Home - could include bar ware
Mens
Baby
Flatware

Target Market(s)

Buyers and potential clients

Industry/Entity Type

Trade

Font styles to use
Serif

Colors
ffffff
ec2027

Requirements
Must have
• It must be a 4 flap flyer which is simple to open and not fancy cut outs.
Nice to have
• The printing will be on the front cover and then on the four flaps inside.
Should not have
• The design must not be in over powering colors. The back ground must be white in order to show the products. The use of color must be subtle and not loud.

```html
<!DOCTYPE html>
<html lang="en">
<head>
<meta charset="utf-8">
<title>Vantorel Silver Gifts – Trade Show Flyer</title>
<link rel="stylesheet" href="https://fonts.googleapis.com/css2?family=Tinos:wght@400;700&display=swap">
<style>
  :root {
    --red: #ec2027;
    --white: #ffffff;
    --black: #0b0b0b;
    --silver: #bdbdbd;
    --silver-light: #d9d9d9;
    --ink: #1a1a1a;
    --serif: "Tinos", "Times New Roman", serif;
  }
  * { box-sizing: border-box; margin: 0; padding: 0; }
  html, body { width: 1200px; height: 900px; overflow: hidden; background: var(--white); }
  body { font-family: var(--serif); color: var(--ink); }

  .flyer { position: relative; width: 1200px; height: 900px; }

  .flap {
    position: absolute; width: 390px; height: 270px;
    background: var(--white); overflow: hidden;
    box-shadow: 0 6px 14px rgba(0,0,0,.28);
  }
  .flap--home    { left: 405px; top: 45px; }
  .flap--cutlery { left: 15px;  top: 317px; }
  .flap--cover   { left: 405px; top: 317px; z-index: 2; }
  .flap--mens    { left: 795px; top: 317px; }
  .flap--baby    { left: 405px; top: 587px; }

  .flap__art { position: absolute; inset: 0; width: 100%; height: 100%; }

  .tab {
    position: absolute; left: 0; top: 16px; height: 17px; padding: 0 22px 0 8px;
    color: var(--white); font-size: 14px; line-height: 17px; letter-spacing: .5px;
    background: var(--red);
    clip-path: polygon(0 0, 100% 0, 86% 100%, 0 100%);
  }

  .product-photo { position: absolute; }

  .price { position: absolute; line-height: 1; white-space: nowrap; }
  .price__was { display: block; font-size: 9px; color: var(--ink); padding-left: 8px; }
  .price__now { display: block; font-size: 24px; color: var(--red); }

  .label { position: absolute; line-height: 1; text-align: center; white-space: nowrap; }
  .label__name { display: block; font-size: 11px; letter-spacing: .3px; text-transform: uppercase; }
  .label__spec { display: block; font-size: 9px; color: #444; }
  .label--left { text-align: left; }
  .label--right { text-align: right; }

  .brand {
    position: absolute; left: 20px; top: 22px;
    display: flex; align-items: center; gap: 6px;
  }
  .brand__dot { width: 14px; height: 14px; border-radius: 50%; background: var(--black); }
  .brand__name { font-size: 16px; color: var(--black); letter-spacing: 1px; line-height: 1; }
  .brand__tagline { position: absolute; left: 40px; top: 42px; font-size: 5px; letter-spacing: .8px; color: #333; }

  .contact {
    position: absolute; right: 20px; bottom: 18px; text-align: right;
    color: var(--white); font-size: 7px; line-height: 1.55; letter-spacing: .3px; text-transform: uppercase;
  }
  .contact__web { font-size: 5px; }

  .badge-text { font-family: var(--serif); fill: var(--white); text-anchor: middle; }
</style>
</head>
<body>
<main class="flyer">

  <section class="flap flap--home">
    <svg class="flap__art" viewBox="0 0 390 270" aria-hidden="true">
      <polygon points="240,0 390,0 390,62" fill="var(--silver-light)"/>
      <polygon points="250,0 390,0 390,40" fill="var(--red)"/>
      <polygon points="0,228 0,270 135,270" fill="var(--silver-light)"/>
    </svg>
    <div class="tab">HOME</div>
    <div class="product-photo" role="img" aria-label="Silver plated candle stand product photo"
         style="left:160px;top:70px;width:70px;height:190px;background:linear-gradient(90deg,#cfcfcf,#fafafa 45%,#a8a8a8);border-radius:30px 30px 8px 8px;"></div>
    <div class="price" style="left:62px;top:112px;"><span class="price__was">U.P. $34</span><span class="price__now">$22</span></div>
    <div class="label" style="left:252px;top:122px;"><span class="label__name">Candle Stand</span><span class="label__spec">Silver Plated</span></div>
  </section>

  <section class="flap flap--cutlery">
    <svg class="flap__art" viewBox="0 0 390 270" aria-hidden="true">
      <polygon points="240,0 390,0 390,30" fill="var(--silver-light)"/>
      <polygon points="255,0 390,0 390,18" fill="var(--red)"/>
      <polygon points="0,240 0,270 130,270" fill="var(--silver-light)"/>
      <polygon points="300,270 390,240 390,270" fill="var(--red)"/>
    </svg>
    <div class="tab">CUTLERY</div>
    <div class="product-photo" role="img" aria-label="Silver plated spoon and fork product photo"
         style="left:115px;top:55px;width:150px;height:150px;background:radial-gradient(ellipse at 50% 45%,#f4f4f4,#bcbcbc 60%,transparent 72%);"></div>
    <div class="price" style="left:55px;top:118px;"><span class="price__was">U.P. $35</span><span class="price__now">$18</span></div>
    <div class="label" style="left:255px;top:132px;"><span class="label__name">Spoon and Fork</span><span class="label__spec">Silver Plated Utensils</span></div>
  </section>

  <section class="flap flap--cover">
    <svg class="flap__art" viewBox="0 0 390 270" aria-hidden="true">
      <rect width="390" height="270" fill="var(--silver)"/>
      <polygon points="0,0 175,0 0,150" fill="var(--white)"/>
      <polygon points="285,0 390,0 390,270 135,270" fill="var(--black)"/>
      <polygon points="360,0 390,0 390,35" fill="var(--red)"/>
      <polygon points="0,220 0,270 45,270" fill="var(--red)"/>
      <g stroke="var(--white)" stroke-width="1.5" fill="var(--red)">
        <polygon points="192,56 224,88 192,120 160,88"/>
        <polygon points="153,94 185,126 153,158 121,126"/>
        <polygon points="227,94 259,126 227,158 195,126"/>
        <polygon points="192,132 224,164 192,196 160,164"/>
      </g>
      <polygon points="190,120 196,126 190,132 184,126" fill="var(--white)"/>
      <text class="badge-text" x="192" y="85" font-size="8">Silver</text>
      <text class="badge-text" x="192" y="98" font-size="12">Gifts</text>
      <text class="badge-text" x="153" y="123" font-size="7">Engravable</text>
      <text class="badge-text" x="153" y="136" font-size="12">Gifts</text>
      <text class="badge-text" x="227" y="123" font-size="8">Easy</text>
      <text class="badge-text" x="227" y="136" font-size="12">Gifts</text>
      <text class="badge-text" x="192" y="161" font-size="12">Silver</text>
      <text class="badge-text" x="192" y="172" font-size="7">Discount</text>
    </svg>
    <div class="brand"><span class="brand__dot"></span><span class="brand__name">vantorel</span></div>
    <div class="brand__tagline">STERLING SILVER GIFTS</div>
    <div class="contact">
      <div>Email : info@vantorel.example</div>
      <div>Buyer Contact: 555-318-2947</div>
      <div class="contact__web">Website: www.vantorel.example</div>
    </div>
  </section>

  <section class="flap flap--mens">
    <svg class="flap__art" viewBox="0 0 390 270" aria-hidden="true">
      <polygon points="240,0 390,0 390,30" fill="var(--silver-light)"/>
      <polygon points="250,0 390,0 390,18" fill="var(--red)"/>
      <polygon points="0,238 0,270 120,270" fill="var(--silver-light)"/>
    </svg>
    <div class="tab">MENS</div>
    <div class="product-photo" role="img" aria-label="Silver business card holder product photo"
         style="left:20px;top:74px;width:170px;height:76px;background:linear-gradient(160deg,#f7f7f7,#cfcfcf 60%,#9d9d9d);transform:skewY(-6deg);"></div>
    <div class="product-photo" role="img" aria-label="Blue and navy enamel cufflinks product photo"
         style="left:205px;top:140px;width:175px;height:125px;background:radial-gradient(ellipse at 50% 55%,#2a3c9c,#1b2470 45%,#c9c9c9 62%,transparent 75%);"></div>
    <div class="price" style="left:255px;top:54px;"><span class="price__was">U.P. $68</span><span class="price__now">$35</span></div>
    <div class="label" style="left:218px;top:92px;"><span class="label__name">Business Card Holder</span><span class="label__spec">Men's Edition</span></div>
    <div class="price" style="left:80px;top:172px;"><span class="price__was">U.P. $90</span><span class="price__now">$48</span></div>
    <div class="label" style="left:28px;top:208px;"><span class="label__name">Blue &amp; Navy Blue Enamel</span><span class="label__spec">Stainless Steel</span></div>
  </section>

  <section class="flap flap--baby">
    <svg class="flap__art" viewBox="0 0 390 270" aria-hidden="true">
      <polygon points="220,0 390,0 390,50" fill="var(--silver-light)"/>
      <polygon points="230,0 390,0 390,28" fill="var(--red)"/>
      <polygon points="0,235 0,270 110,270" fill="var(--red)"/>
    </svg>
    <div class="tab">BABY</div>
    <div class="product-photo" role="img" aria-label="Silver baby cup product photo"
         style="left:108px;top:60px;width:115px;height:90px;background:linear-gradient(90deg,#bdbdbd,#f8f8f8 45%,#a5a5a5);border-radius:6px 6px 14px 14px;"></div>
    <div class="product-photo" role="img" aria-label="Silver baby rattle product photo"
         style="left:170px;top:140px;width:80px;height:95px;border-radius:40px;background:radial-gradient(circle at 40% 35%,#ffffff,#cacaca 55%,#8e8e8e);transform:rotate(40deg);"></div>
    <div class="price" style="left:18px;top:92px;"><span class="price__was">U.P. $88</span><span class="price__now">$45</span></div>
    <div class="label label--left" style="left:18px;top:130px;"><span class="label__name">Silverish Cup</span><span class="label__spec">Stainless Glass</span></div>
    <div class="price" style="left:325px;top:183px;"><span class="price__was">U.P. $90</span><span class="price__now">$48</span></div>
    <div class="label label--right" style="right:25px;top:222px;"><span class="label__name">Silverish Rattle</span><span class="label__spec">Stainless Steel</span></div>
  </section>

</main>
</body>
</html>
```